Graphic background for 10 Pull Up Banners

To produce a graphic background for a 100 cm wide by 200 cm high Pull-Up Display banner containing a Buddhist text in three languages: Tibetan, Mandarin and English. Please refer to uploaded file "Elements of Pull Up Banner". The design should be simple (not drawing attention away from the text). This design should then be varied for or extended to the next banner and so on until the 10th banner. When the banners are lined up, they should form a single design that is 1000 cm wide by 200 cm high.
An alternative way to look at the project is to produce a graphic background of 1000 cm width by 200 cm height that is then splitted into ten separate 100 cm wide by 200 cm high graphic to be used as background for 10 Buddhist texts (text 1, 2, 3, 4, 5, 6, 7, 8, 9a, 9b) on 10 Pull-Up Display Banners, the text in each banner being in the three languages mentioned earlier.
In either perspective, the design should be simple and not draw attention away from the texts. See uploaded PDF file "Examples.pdf"
For attendees at a Buddhist Event.

```html
<!DOCTYPE html>
<html lang="en">
<head>
<meta charset="utf-8">
<title>Ten Mistaking</title>
<link rel="stylesheet" href="https://fonts.googleapis.com/css2?family=Marcellus&family=Noto+Serif+Tibetan:wght@400;600&family=Noto+Sans+SC:wght@400&family=Noto+Serif+SC:wght@500&family=Tinos&display=swap">
<style>
  :root {
    --lime-top: #9fd23f;
    --lime-mid: #b3d84a;
    --lime-low: #c7d63c;
    --gold-low: #d7b52a;
    --amber-edge: #f2a21a;
    --crimson: #b5123c;
    --crimson-dark: #8e1030;
    --panel: rgba(255, 255, 240, 0.32);
    --panel-strong: rgba(255, 250, 215, 0.55);
    --frame: #ffffff;
    --wheel: rgba(250, 245, 190, 0.35);
    --leaf: #79c23a;
  }
  * { box-sizing: border-box; margin: 0; padding: 0; }
  html, body { width: 1200px; height: 2375px; overflow: hidden; }
  body { background: var(--lime-mid); }
  .banner {
    position: relative;
    width: 1200px;
    height: 2375px;
    overflow: hidden;
    background: linear-gradient(180deg, var(--lime-top) 0%, var(--lime-mid) 45%, var(--lime-low) 70%, var(--gold-low) 100%);
    border-left: 9px solid var(--amber-edge);
  }
  .backdrop { position: absolute; inset: 0; }
  .deity {
    position: absolute;
    left: 171px; top: 108px;
    width: 233px; height: 272px;
    background: radial-gradient(ellipse at 50% 45%, #e8a0a0 0%, #c94a5a 55%, rgba(180, 30, 60, 0.15) 100%);
    border-radius: 40% 40% 8px 8px;
    opacity: 0.75;
  }
  .title {
    position: absolute;
    left: 418px; top: 168px;
    font-family: "Marcellus", serif;
    font-size: 128px;
    line-height: 1;
    color: var(--crimson);
    letter-spacing: 1px;
  }
  .text-panel {
    position: absolute;
    left: 237px; width: 732px;
    background: var(--panel);
    text-align: center;
    color: var(--crimson);
  }
  .text-panel--tibetan { top: 462px; height: 410px; padding-top: 48px; }
  .text-panel--chinese { top: 937px; height: 410px; padding-top: 18px; }
  .text-panel--english { top: 1422px; height: 411px; padding-top: 58px; }
  .tibetan-verse {
    font-family: "Noto Serif Tibetan", serif;
    font-size: 17px;
    line-height: 28px;
    color: var(--crimson-dark);
  }
  .chinese-verse {
    font-family: "Noto Sans SC", sans-serif;
    font-size: 23px;
    line-height: 28.5px;
  }
  .footnotes {
    margin-top: 80px;
    font-family: "Noto Sans SC", sans-serif;
    font-size: 9px;
    line-height: 15px;
  }
  .english-verse {
    font-family: "Tinos", serif;
    font-size: 16px;
    line-height: 28.5px;
  }
  .dedication {
    position: absolute;
    left: 237px; top: 1963px;
    width: 729px; height: 282px;
    background: var(--panel-strong);
    text-align: center;
    color: var(--crimson);
  }
  .dedication__frame {
    position: absolute;
    left: 24px; top: 16px; right: 24px; bottom: 13px;
    border: 2px solid var(--crimson-dark);
  }
  .dedication__tibetan {
    position: absolute; left: 0; right: 0; top: 52px;
    font-family: "Noto Serif Tibetan", serif;
    font-weight: 600;
    font-size: 34px;
    line-height: 1;
  }
  .dedication__chinese {
    position: absolute; left: 0; right: 0; top: 120px;
    font-family: "Noto Serif SC", serif;
    font-weight: 500;
    font-size: 38px;
    line-height: 1;
  }
  .dedication__english {
    position: absolute; left: 0; right: 0; top: 178px;
    font-family: "Tinos", serif;
    font-size: 35px;
    line-height: 1;
  }
</style>
</head>
<body>
<main class="banner">
  <svg class="backdrop" width="1200" height="2375" viewBox="0 0 1200 2375">
    <defs>
      <linearGradient id="sweep" x1="0" y1="0" x2="0" y2="1">
        <stop offset="0" stop-color="#e6d94a" stop-opacity="0.5"/>
        <stop offset="1" stop-color="#b58a2a" stop-opacity="0.85"/>
      </linearGradient>
    </defs>
    <path d="M0 1560 C 300 1640, 700 1500, 1200 1640 L1200 2375 L0 2375 Z" fill="#e0e25a" opacity="0.25"/>
    <path d="M0 1900 C 350 1780, 800 2000, 1200 1860 L1200 2375 L0 2375 Z" fill="url(#sweep)"/>
    <g role="img" aria-label="Faint dharma wheel decorations" fill="var(--wheel)">
      <circle cx="690" cy="110" r="130"/>
      <circle cx="1000" cy="480" r="140"/>
      <circle cx="200" cy="610" r="125"/>
      <circle cx="520" cy="850" r="80"/>
      <circle cx="900" cy="880" r="65"/>
      <circle cx="280" cy="1050" r="70"/>
      <circle cx="160" cy="1395" r="120"/>
      <circle cx="1050" cy="1340" r="105"/>
      <circle cx="350" cy="1640" r="130"/>
      <circle cx="900" cy="1900" r="110"/>
    </g>
    <g role="img" aria-label="Scattered bodhi leaves" fill="var(--leaf)" opacity="0.85">
      <ellipse cx="90" cy="60" rx="70" ry="45"/>
      <ellipse cx="1080" cy="70" rx="85" ry="60"/>
      <ellipse cx="1140" cy="235" rx="45" ry="28"/>
      <ellipse cx="580" cy="375" rx="70" ry="38" opacity="0.5"/>
      <ellipse cx="170" cy="760" rx="28" ry="20"/>
      <ellipse cx="85" cy="1100" rx="70" ry="45"/>
      <ellipse cx="1060" cy="1645" rx="55" ry="32" fill="#d6f06a"/>
      <ellipse cx="115" cy="2000" rx="40" ry="55"/>
      <ellipse cx="1080" cy="2040" rx="90" ry="60" fill="#cdea55"/>
      <ellipse cx="80" cy="2280" rx="90" ry="70"/>
    </g>
    <path class="frame" fill="none" stroke="var(--frame)" stroke-width="3"
      d="M107 32 H1093 A63 63 0 0 0 1156 95 V2277 A63 63 0 0 0 1093 2340 H107 A63 63 0 0 0 44 2277 V95 A63 63 0 0 0 107 32 Z"/>
  </svg>

  <div class="deity" role="img" aria-label="Painted Buddhist deity on a lotus throne"></div>
  <h1 class="title">Ten Mistaking</h1>

  <section class="text-panel text-panel--tibetan" lang="bo">
    <p class="tibetan-verse">
      དད་པ་དང་འདོད་པ་ལ་ནོར་ས་ཡོད།<br>
      བྱམས་སྙིང་རྗེ་དང་ཆགས་པ་ལ་ནོར་ས་ཡོད།<br>
      ཤེས་བྱའི་སྟོང་པ་དང་བློས་བྱས་ཀྱི་སྟོང་པ་ལ་ནོར་ས་ཡོད།<br>
      ཆོས་ཀྱི་དབྱིངས་དང་ཆད་ལྟ་ལ་ནོར་ས་ཡོད།<br>
      ཉམས་མྱོང་དང་རྟོགས་པ་ལ་ནོར་ས་ཡོད།<br>
      བཙུན་པ་དང་ཆོས་འཆོས་པ་ལ་ནོར་ས་ཡོད།<br>
      འཁྲུལ་ཞིག་དང་བདུད་ཀྱིས་ཟིན་པ་ལ་ནོར་ས་ཡོད།<br>
      གྲུབ་ཐོབ་དང་ཟོལ་ཅན་ལ་ནོར་ས་ཡོད།<br>
      གཞན་དོན་དང་རང་དོན་ལ་ནོར་ས་ཡོད།<br>
      ཐབས་མཁས་དང་གཡོ་སྒྱུ་ལ་ནོར་ས་ཡོད།
    </p>
  </section>

  <section class="text-panel text-panel--chinese" lang="zh">
    <p class="chinese-verse">
      .信心与爱欲可能混淆，<br>
      慈悲与贪执可能混淆，<br>
      所知1本空与思维造作空性可能混淆，<br>
      法界与断见2可能混淆，<br>
      觉受与证悟可能混淆，<br>
      尊者与神棍可能混淆，<br>
      破惑与著魔可能混淆，<br>
      成就者与骗子可能混淆，<br>
      利他与自利可能混淆，<br>
      方便善巧与谄媚哄骗可能混淆。
    </p>
    <p class="footnotes">
      1：所知：可以认识的外境。<br>
      2：断见：否定因果、前生、后世等说法的见解
    </p>
  </section>

  <section class="text-panel text-panel--english" lang="en">
    <p class="english-verse">
      Desire can be mistaken for faith or devotion.<br>
      Attachment can be mistaken for love and compassion.<br>
      Conceptual emptiness can be mistaken for the emptiness of the nature of phenomena.<br>
      Nihilism can be mistaken for the dharmadhatu.<br>
      A meditative experience can be mistaken for realization.<br>
      Outer religious practices can be mistaken for inner development of good qualities.<br>
      A person in the grip of a demon can be mistaken for a person who has destroyed his own delusions.<br>
      A charlatan can be mistaken for a siddha.<br>
      An act to benefit yourself can be mistaken for an act to benefit others.<br>
      Deviousness can be mistaken for skilful means.
    </p>
  </section>

  <section class="dedication">
    <div class="dedication__frame"></div>
    <p class="dedication__tibetan" lang="bo">སེམས་ཅན་ཐམས་ཅད་སངས་རྒྱས་ཐོབ་པར་ཤོག</p>
    <p class="dedication__chinese" lang="zh">愿诸有情共证佛果位</p>
    <p class="dedication__english">May all attain Buddhahood together.</p>
  </section>
</main>
</body>
</html>
```